Design a label for horse salt

I need a label for the packaging for horse salt.

Label size is 99.1mm x 67.7mm

Information on the label includes:

Not for Human Consumption
SALT
Approx 530gms
Ingredients: 100% Additive Free Natural Solar Sea Salt
Packed in Queensland by Brindlecove Horse Feed

You may also include other interesting marketing or facts at your discretion (subject to approval)

I would like a background image included.

included is the logo for the Brindlecove Horse Feed.

```html
<!DOCTYPE html>
<html lang="en">
<head>
<meta charset="utf-8">
<title>Horse Salt Label</title>
<link href="https://fonts.googleapis.com/css2?family=Abril+Fatface&family=Montserrat:wght@400;500;600;700&display=swap" rel="stylesheet">
<style>
  :root {
    --backdrop: #d0d673;
    --label-black: #0b0b0b;
    --stripe: #141414;
    --white: #ffffff;
    --salt-red: #ee1c25;
    --copper: #c8875a;
    --badge-orange: #f7941d;
    --horse-light: #b5642e;
    --horse-mid: #7a3a17;
    --horse-dark: #1a0d07;
  }
  html, body {
    margin: 0;
    padding: 0;
    width: 1200px;
    height: 749px;
    overflow: hidden;
    background: var(--backdrop);
    font-family: "Montserrat", Arial, sans-serif;
  }
  .label {
    position: absolute;
    left: 96px;
    top: 30px;
    width: 1008px;
    height: 688px;
    overflow: hidden;
    background:
      repeating-linear-gradient(90deg, var(--label-black) 0 9px, var(--stripe) 9px 10px);
    color: var(--white);
  }
  .horse-art {
    position: absolute;
    left: 0;
    top: 0;
    width: 1008px;
    height: 688px;
  }
  .brand-name {
    position: absolute;
    left: 0;
    width: 610px;
    top: 74px;
    text-align: center;
    font-size: 20px;
    font-weight: 600;
    color: var(--white);
    display: flex;
    justify-content: center;
    align-items: center;
    gap: 10px;
  }
  .brand-name .dot {
    width: 14px;
    height: 14px;
    border-radius: 50%;
    background: var(--white);
  }
  .warning-pill {
    position: absolute;
    left: 98px;
    top: 197px;
    width: 425px;
    height: 88px;
    box-sizing: border-box;
    border: 3px solid var(--white);
    border-radius: 44px;
    text-align: center;
    display: flex;
    flex-direction: column;
    justify-content: center;
    line-height: 1.2;
    font-size: 28px;
  }
  .warning-pill strong { font-weight: 600; }
  .product-name {
    position: absolute;
    left: 0;
    width: 624px;
    top: 262px;
    text-align: center;
    font-family: "Abril Fatface", Georgia, serif;
    font-size: 228px;
    line-height: 1;
    color: var(--salt-red);
    margin: 0;
    font-weight: 400;
  }
  .weight {
    position: absolute;
    left: 0;
    width: 624px;
    top: 494px;
    text-align: center;
    line-height: 1.1;
  }
  .weight .approx { font-size: 26px; font-weight: 500; display: block; }
  .weight .grams { font-size: 42px; font-weight: 600; display: block; }
  .packer {
    position: absolute;
    left: 0;
    width: 624px;
    top: 594px;
    text-align: center;
    font-size: 22px;
    line-height: 1.5;
    color: var(--copper);
  }
  .badge {
    position: absolute;
    left: 0;
    top: 0;
    width: 1008px;
    height: 688px;
  }
  .badge .pct {
    font-family: "Montserrat", Arial, sans-serif;
    font-weight: 500;
    fill: var(--badge-orange);
    filter: drop-shadow(0 0 6px rgba(247,148,29,0.6));
  }
  .badge .additive {
    font-family: "Montserrat", Arial, sans-serif;
    font-weight: 500;
    fill: var(--badge-orange);
  }
  .badge .arc-text {
    font-family: "Montserrat", Arial, sans-serif;
    font-weight: 500;
    fill: var(--white);
    letter-spacing: 1px;
  }
</style>
</head>
<body>
<main class="label">
  <svg class="horse-art" viewBox="0 0 1008 688" role="img" aria-label="Photograph of a chestnut horse's head with a white blaze, framed in an oval">
    <defs>
      <radialGradient id="horseTone" cx="0.55" cy="0.45" r="0.6">
        <stop offset="0" stop-color="var(--horse-light)"/>
        <stop offset="0.55" stop-color="var(--horse-mid)"/>
        <stop offset="1" stop-color="var(--horse-dark)"/>
      </radialGradient>
    </defs>
    <ellipse cx="840" cy="180" rx="224" ry="220" fill="url(#horseTone)"/>
    <ellipse cx="840" cy="180" rx="228" ry="224" fill="none" stroke="var(--white)" stroke-width="3"/>
  </svg>

  <div class="brand-name"><span class="dot"></span>Brindlecove Horse Feed</div>

  <div class="warning-pill">
    <span>Not for</span>
    <strong>Human Consumption</strong>
  </div>

  <h1 class="product-name">SALT</h1>

  <div class="weight">
    <span class="approx">Approx</span>
    <span class="grams">530gms</span>
  </div>

  <div class="packer">
    Packed in Queensland Australia<br>
    by Brindlecove Horse Feed
  </div>

  <svg class="badge" viewBox="0 0 1008 688">
    <defs>
      <path id="tooth" d="M122 0 L112.86 5.54 L121.41 11.96" fill="none" stroke="#ffffff" stroke-width="2"/>
      <g id="t2"><use href="#tooth"/><use href="#tooth" transform="rotate(5.625)"/></g>
      <g id="t4"><use href="#t2"/><use href="#t2" transform="rotate(11.25)"/></g>
      <g id="t8"><use href="#t4"/><use href="#t4" transform="rotate(22.5)"/></g>
      <g id="t16"><use href="#t8"/><use href="#t8" transform="rotate(45)"/></g>
      <g id="t32"><use href="#t16"/><use href="#t16" transform="rotate(90)"/></g>
      <path id="badgeArc" d="M-142 0 A142 142 0 0 0 142 0"/>
    </defs>
    <g transform="translate(784 526)">
      <use href="#t32"/>
      <use href="#t32" transform="rotate(180)"/>
      <path d="M-14 -44 C-14 -62 2 -72 18 -74 C18 -58 10 -44 -6 -42 M-12 -42 L4 -60" fill="var(--white)" stroke="var(--white)" stroke-width="2" stroke-linecap="round"/>
      <text class="pct" x="0" y="16" text-anchor="middle" font-size="64">100%</text>
      <text class="additive" x="0" y="48" text-anchor="middle" font-size="26">Additive Free</text>
      <text class="arc-text" font-size="22" text-anchor="middle">
        <textPath href="#badgeArc" startOffset="50%">Natural Solar Sea Salt</textPath>
      </text>
    </g>
  </svg>
</main>
</body>
</html>
```